A 24' X 36" SIGN TO ANNOUNCE "ORDER EARLY FOR THE HOLIDAYS

sign is to announce order "early for the holidays"
The design should be festive and leaning towards nostalgic and antique. We are a 100yr old butcher shop. Sign is to list options for customers to include
gkbn prime filet mignon
prime rib roast
goose
duck
pheasant
crown roast of pork/lamb
spiral cut smoked hams
sign should have a black backround
also include or logo
Font styles to use
Serif

```html
<!DOCTYPE html>
<html lang="en">
<head>
<meta charset="utf-8">
<title>Order Early for the Holidays</title>
<link rel="stylesheet" href="https://fonts.googleapis.com/css2?family=Playfair+Display+SC:wght@700;900&family=Lato:wght@400;700&family=Yellowtail&display=swap">
<style>
  :root {
    --page: #eeeeee;
    --sign-black: #000000;
    --gold: #f7e12a;
    --white: #ffffff;
    --pine: #1f7a3a;
    --berry: #8e1a1a;
  }
  * { margin: 0; padding: 0; box-sizing: border-box; }
  html, body { width: 1200px; height: 1000px; overflow: hidden; }
  body { background: var(--page); position: relative; font-family: "Lato", sans-serif; }

  .sign {
    position: absolute; left: 292px; top: 14px; width: 644px; height: 968px;
    background: var(--sign-black);
  }
  .sign__frame { position: absolute; inset: 0; }

  .decor { position: absolute; }
  .decor--garland {
    left: 30px; top: 32px; width: 584px; height: 290px;
    background: radial-gradient(ellipse at 50% 0%, rgba(31,122,58,0.55) 0%, rgba(142,26,26,0.28) 45%, rgba(0,0,0,0) 75%);
  }
  .decor--holly-left, .decor--holly-right {
    bottom: 30px; height: 190px;
    background: radial-gradient(ellipse at 50% 100%, rgba(31,122,58,0.6) 0%, rgba(142,26,26,0.3) 50%, rgba(0,0,0,0) 78%);
  }
  .decor--holly-left { left: 30px; width: 254px; }
  .decor--holly-right { right: 30px; width: 202px; }

  .brand {
    position: absolute; left: 0; right: 0; top: 102px; text-align: center;
    font-family: "Playfair Display SC", serif; font-weight: 700; font-size: 19px;
    letter-spacing: 2px; color: var(--gold);
  }

  .headline {
    position: absolute; left: 0; right: 0; top: 172px; text-align: center;
    font-family: "Playfair Display SC", serif; font-weight: 900; font-size: 82px;
    letter-spacing: 4px; color: var(--gold); line-height: 1;
  }

  .subhead {
    position: absolute; left: 0; right: 0; top: 268px;
    display: flex; justify-content: center; align-items: center; gap: 12px;
    font-family: "Lato", sans-serif; font-size: 29px; color: var(--gold); letter-spacing: 0.5px;
  }
  .subhead__rule { width: 46px; height: 12px; display: block; }

  .script {
    position: absolute; left: 0; right: 0; top: 300px; text-align: center;
    font-family: "Yellowtail", cursive; font-size: 150px; line-height: 1.1;
    color: var(--gold);
  }

  .menu {
    position: absolute; left: 0; right: 0; top: 484px; list-style: none; text-align: center;
    font-family: "Lato", sans-serif; font-weight: 700; font-size: 27px; line-height: 35.5px;
    color: var(--white); letter-spacing: 0.5px;
  }
  .menu__star { font-size: 16px; vertical-align: 3px; margin: 0 8px; }
</style>
</head>
<body>
  <div class="sign">
    <div class="decor decor--garland" role="img" aria-label="Sketched pine garland with red poinsettias, bows and hanging ornaments"></div>
    <div class="decor decor--holly-left" role="img" aria-label="Sketched holly leaves with red ornament baubles"></div>
    <div class="decor decor--holly-right" role="img" aria-label="Sketched holly leaves with red ornament baubles"></div>

    <svg class="sign__frame" width="644" height="968" viewBox="0 0 644 968" aria-hidden="true">
      <path d="M36 24 H608 A12 12 0 0 0 620 36 V932 A12 12 0 0 0 608 944 H36 A12 12 0 0 0 24 932 V36 A12 12 0 0 0 36 24 Z"
            fill="none" stroke="var(--gold)" stroke-width="3"/>
      <path d="M42 32 H602 A10 10 0 0 0 612 42 V926 A10 10 0 0 0 602 936 H42 A10 10 0 0 0 32 926 V42 A10 10 0 0 0 42 32 Z"
            fill="none" stroke="var(--gold)" stroke-width="1.5"/>
    </svg>

    <div class="brand">HALLORAN MARKET</div>

    <h1 class="headline">ORDER</h1>

    <div class="subhead">
      <svg class="subhead__rule" viewBox="0 0 46 12" aria-hidden="true">
        <g stroke="var(--gold)" stroke-width="1.5"><line x1="14" y1="1" x2="46" y2="1"/><line x1="6" y1="4.5" x2="46" y2="4.5"/><line x1="0" y1="8" x2="46" y2="8"/><line x1="10" y1="11.5" x2="46" y2="11.5"/></g>
      </svg>
      <span>EARLY FOR THE</span>
      <svg class="subhead__rule" viewBox="0 0 46 12" aria-hidden="true">
        <g stroke="var(--gold)" stroke-width="1.5"><line x1="0" y1="1" x2="32" y2="1"/><line x1="0" y1="4.5" x2="40" y2="4.5"/><line x1="0" y1="8" x2="46" y2="8"/><line x1="0" y1="11.5" x2="36" y2="11.5"/></g>
      </svg>
    </div>

    <div class="script">holidays</div>

    <ul class="menu">
      <li><span class="menu__star">★</span>GKBN PRIME FILET MIGNON<span class="menu__star">★</span></li>
      <li><span class="menu__star">★</span>PRIME RIB ROAST<span class="menu__star">★</span></li>
      <li><span class="menu__star">★</span>GOOSE<span class="menu__star">★</span></li>
      <li><span class="menu__star">★</span>DUCK<span class="menu__star">★</span></li>
      <li><span class="menu__star">★</span>PHEASANT<span class="menu__star">★</span></li>
      <li><span class="menu__star">★</span>CROWN ROAST OF PORK/LAMB<span class="menu__star">★</span></li>
      <li><span class="menu__star">★</span>SPIRAL CUT SMOKED HAMS<span class="menu__star">★</span></li>
    </ul>
  </div>
</body>
</html>
```